smile partners of lakeview | ||
business cards/stationary | ||
Cutting-Edge Professional |
Dr. Marcus Holloway / Dr. Leonardo Brisco | ||
President | ||
Bayonne 57 Ave K Harborview, NJ 08411 201-555-0142 ********* East Orange 42 North Whitfield St Suite 208 East Alder, NJ 08437 973-555-0187 ******** North Bergen 4829 Larkmoor North Ridgeway, NJ 08452 201-555-0163 ********** Union City 2748 Quenton Ave Millbrook, NJ 08426 201-555-0129 ********* Paterson 3170 Elm street Suite K Falconer, NJ 08463 973 555-0114 ******** |
office@quentondental.example | ||
www.SmilePartnersOfLV.example | ||
We need 7 different business card designs. 1. Dr Marcus Holloway (no address..just website) 2. Dr Leonardo Brisco (no address just website) 3. Smile Partners of Lakeview - East Orange 4. Smile Partners of Lakeview - Bayone 5. Smile Partners of Lakeview- Union City 6. Smile Partners of Lakeview- North Bergen 7. Smile Partners of Lakeview- Paterson Business Cards 3-7 do not need to include Dr Holloway/Dr Brisco's name on them |
For the personal cards (Dr Marcus Holloway and Dr Leo Brisco) use the back of the cards to tell all of the office locations For the Office cards (3-7) use the back of the card for appointments...we will upload a sample background that we currently use. |
554611_1195_4351.png |
photo3_JPG4352.jpg |
DentalGroups_Paterson_4421.pdf |
DentalGroups_Paterson_4422.gif |
DentalGroups_Paterson_4423.eps |
DentalGroups_Web_4424.png |
DentalGroups_Web_4425.ai |
DentalGroups_Web_4426.gif |

```html
<!DOCTYPE html>
<html lang="en">
<head>
<meta charset="utf-8">
<title>Smile Partners of Lakeview – Business Card</title>
<link href="https://fonts.googleapis.com/css2?family=Cardo:wght@400;700&display=swap" rel="stylesheet">
<style>
  :root {
    --backdrop: #efe9df;
    --brown: #5b2711;
    --logo-brown: #84441a;
    --card-white: #ffffff;
    --cream: #f3e7d3;
  }
  html, body {
    margin: 0;
    padding: 0;
    width: 1200px;
    height: 802px;
    overflow: hidden;
    background: var(--backdrop);
    font-family: "Cardo", serif;
  }
  .canvas { position: relative; width: 1200px; height: 802px; }
  .card {
    position: absolute;
    left: 252px;
    width: 888px;
    background: var(--card-white);
    overflow: hidden;
  }
  /* Front */
  .card-front { top: 12px; height: 380px; }
  .front-band-top {
    position: absolute; left: 0; top: 0; width: 100%; height: 89px;
    background: var(--brown);
  }
  .holder {
    position: absolute; right: 22px; top: 14px;
    text-align: right; color: var(--cream);
  }
  .holder-name { font-size: 22px; line-height: 1.1; }
  .holder-title { font-size: 8px; letter-spacing: 1px; text-transform: uppercase; font-weight: 700; }
  .wordmark { position: absolute; text-align: center; color: var(--logo-brown); }
  .wordmark-front { left: 220px; width: 440px; top: 205px; }
  .wordmark-line1 { font-size: 50px; line-height: 1; }
  .wordmark-line2 { font-size: 40px; line-height: 1.05; }
  .website { font-size: 10px; color: var(--brown); margin-top: 4px; font-weight: 700; }
  /* Back */
  .card-back { top: 410px; height: 382px; background: var(--brown); }
  .back-strip {
    position: absolute; left: 0; top: 0; width: 100%; height: 98px;
    background: var(--card-white);
  }
  .wordmark-back { left: 260px; width: 220px; top: 26px; }
  .wordmark-back .wordmark-line1 { font-size: 26px; }
  .wordmark-back .wordmark-line2 { font-size: 20px; }
  .office {
    position: absolute; color: var(--cream);
    font-size: 12px; line-height: 1.3;
  }
  .office-name::before { content: "\2605\00a0"; font-size: 10px; }
</style>
</head>
<body>
<div class="canvas">
  <section class="card card-front">
    <div class="front-band-top"></div>
    <div class="holder">
      <div class="holder-name">Dr. Leonardo Brisco</div>
      <div class="holder-title">President</div>
    </div>
    <div class="wordmark wordmark-front">
      <div class="wordmark-line1">Smile Partners</div>
      <div class="wordmark-line2">of Lakeview</div>
      <div class="website">www.SmilePartnersOfLV.example</div>
    </div>
  </section>

  <section class="card card-back">
    <div class="back-strip">
      <div class="wordmark wordmark-back">
        <div class="wordmark-line1">Smile Partners</div>
        <div class="wordmark-line2">of Lakeview</div>
      </div>
    </div>
    <div class="office" style="left:96px; top:170px;">
      <div class="office-name">Harborview</div>
      <div>57 Ave K</div>
      <div>Harborview, NJ 08411</div>
      <div>201-555-0142</div>
    </div>
    <div class="office" style="left:259px; top:170px;">
      <div class="office-name">Millbrook</div>
      <div>2748 Quenton Ave</div>
      <div>Millbrook, NJ 08426</div>
      <div>201-555-0129</div>
    </div>
    <div class="office" style="left:439px; top:170px;">
      <div class="office-name">East Alder</div>
      <div>42 North Whitfield St</div>
      <div>Suite 208</div>
      <div>East Alder, NJ 08437</div>
      <div>973-555-0187</div>
    </div>
    <div class="office" style="left:187px; top:256px;">
      <div class="office-name">North Ridgeway</div>
      <div>4829 Larkmoor</div>
      <div>North Ridgeway, NJ 08452</div>
      <div>201-555-0163</div>
    </div>
    <div class="office" style="left:379px; top:256px;">
      <div class="office-name">Falconer</div>
      <div>3170 Elm street</div>
      <div>Suite K</div>
      <div>Falconer, NJ 08463</div>
      <div>973 555-0114</div>
    </div>
  </section>
</div>
</body>
</html>
```